Commercial Real Estate Company Needs Website Redesign

Velcaro is a commercial real estate firm that is based in San Diego, but has offices and properties across the U.S. The current website was completed almost 3 years ago and is need of a refresh. We will rework the existing Wordpress CMS system, but require a new design. We have a great programmer who can take the design into wordpress. I need a design template for each page types, There are are approximately 20 pages for each section of our site. There are 4 Sections: Corporate, Hospitality, Commercial/Residential, and Receiver/Bankruptcy. See attached creative brief for the initial pages we would like drafted.

Industry/Entity Type

Real Estate

```html
<!DOCTYPE html>
<html lang="en">
<head>
<meta charset="utf-8">
<title>Velcaro — Commercial Real Estate</title>
<link href="https://fonts.googleapis.com/css2?family=Roboto:ital,wght@0,300;0,400;0,500;1,300&display=swap" rel="stylesheet">
<style>
:root{
  --navy:#1b2550;
  --orange:#f9a63a;
  --orange-dark:#e2922a;
  --gold-text:#f6b73c;
  --sky-1:#a9c6e6;
  --sky-2:#d9e6f3;
  --panel:#ebebeb;
  --cream:#f7e2a1;
  --blue-btn:#4a84c6;
  --heading-blue:#4a84c6;
  --text:#555;
  --title:#1b2550;
  --white:#fff;
}
*{box-sizing:border-box;margin:0;padding:0}
html,body{width:1200px;height:1102px;overflow:hidden;background:var(--white);font-family:'Roboto',sans-serif}
.page{position:relative;width:1200px;height:1102px}

.site-header{position:absolute;left:0;top:0;width:1200px;height:134px;background:var(--navy)}
.brand{position:absolute;left:104px;top:42px;display:flex;align-items:center;gap:14px}
.brand-mark{width:22px;height:22px;border-radius:50%;background:var(--orange)}
.brand-name{color:var(--white);font-size:42px;font-weight:400;letter-spacing:1px;line-height:1}
.phone{position:absolute;left:781px;top:31px;display:flex;align-items:center;gap:12px;color:var(--white);font-size:20px}
.phone svg{width:22px;height:22px}
.social{position:absolute;top:25px;display:block;width:32px;height:32px;border-radius:50%}
.social.one{left:988px;background:#3b5998}
.social.two{left:1028px;background:#1da1f2}
.social.three{left:1068px;background:#d8cfc9}
.main-nav{position:absolute;top:88px;left:512px;display:flex;gap:18px;font-size:15px;color:var(--white);white-space:nowrap}
.main-nav .active{color:var(--gold-text)}
.dropdown{position:absolute;left:499px;top:118px;width:142px;background:var(--orange);box-shadow:0 2px 4px rgba(0,0,0,.3);z-index:3}
.dropdown li{list-style:none;font-size:11px;color:var(--white);padding:0 21px;height:24px;line-height:26px;border-bottom:1px solid #fbc071}
.dropdown li.current{background:var(--orange-dark)}
.dropdown li:last-child{border-bottom:0}

.hero{position:absolute;left:0;top:134px;width:1200px;height:411px;background:linear-gradient(90deg,var(--sky-1),var(--sky-2) 50%,var(--sky-1))}
.hero-media{position:absolute;left:100px;top:0;width:668px;height:411px;background:linear-gradient(180deg,#6f9fd8 0%,#b8d1ec 38%,#c9ccc9 62%,#6f8a82 85%,#3d4b47 100%)}
.hero-caption{position:absolute;left:100px;top:356px;width:668px;height:55px;background:rgba(20,22,28,.78);color:var(--white);font-size:22px;font-weight:300;padding:13px 19px}
.hero-arrows{position:absolute;right:16px;top:18px;width:28px;height:18px}
.consult{position:absolute;left:768px;top:0;width:336px;height:299px;background:var(--panel);padding:16px 20px 0 17px}
.consult h2{font-size:18px;font-weight:500;color:var(--heading-blue);margin-left:3px;margin-bottom:23px}
.field{display:flex;height:42px;margin-bottom:4px;background:var(--white)}
.field.tall{height:43px}
.field .ico{width:47px;background:var(--orange);display:flex;align-items:center;justify-content:center}
.field .ico svg{width:16px;height:16px}
.field .ico.big svg{width:20px;height:20px}
.field span{padding:13px 16px;font-size:15px;color:#555}
.field.tall span{padding-top:8px}
.submit{display:block;margin:14px 0 0 111px;width:84px;height:31px;background:var(--orange);color:var(--white);font-size:14px;text-align:center;line-height:31px;border:1px solid #e39630}
.newsletter{position:absolute;left:768px;top:299px;width:336px;height:112px;background:var(--cream);padding:18px 17px}
.newsletter h3{font-size:16px;font-weight:500;color:#222;margin-bottom:13px}
.news-row{display:flex;gap:6px}
.news-input{width:201px;height:38px;background:var(--white);border:1px solid #c9c0a6;font-size:14px;font-style:italic;font-weight:300;color:#666;padding:10px 16px}
.news-btn{width:92px;height:38px;background:var(--blue-btn);color:var(--white);font-size:14px;text-align:center;line-height:36px;border:1px solid #3d6fab}
.hero-shadow{position:absolute;left:100px;top:545px;width:1004px;height:14px;background:radial-gradient(ellipse at top,rgba(0,0,0,.18),rgba(0,0,0,0) 70%)}

.services{position:absolute;left:0;top:580px;width:1200px}
.service{position:absolute;width:320px}
.service .photo{width:319px;height:173px}
.service h3{font-size:19px;font-weight:400;color:var(--title);margin:20px 0 15px 1px;letter-spacing:.3px}
.service p{font-size:13px;line-height:22px;color:var(--text);padding-left:4px}

.site-footer{position:absolute;left:0;top:953px;width:1200px;height:149px;background:var(--navy)}
.footer-brand{position:absolute;left:108px;top:52px;display:flex;align-items:center;gap:8px}
.footer-brand .brand-mark{width:12px;height:12px}
.footer-brand .brand-name{font-size:22px}
.copyright{position:absolute;left:104px;top:94px;color:var(--white);font-size:13px}
.address{position:absolute;right:99px;top:53px;color:var(--white);font-size:13px;line-height:22px;text-align:right}
</style>
</head>
<body>
<div class="page">
  <header class="site-header">
    <div class="brand"><span class="brand-mark"></span><span class="brand-name">VELCARO</span></div>
    <div class="phone">
      <svg viewBox="0 0 22 22"><rect width="22" height="22" rx="3" fill="#f9a63a"/><path d="M7 5c1 0 2 2.5 1.6 3.2L7.8 9.3c.8 1.8 2.2 3.3 4 4.1l1-.9c.7-.5 3.2.6 3.2 1.6 0 1.5-1.5 2.9-3 2.4C9.3 15.3 6.7 12.7 5.6 8.6 5.1 7.1 5.6 5 7 5z" fill="#1b2550"/></svg>
      <span>619-555-0148</span>
    </div>
    <a class="social one" aria-label="Social link"></a>
    <a class="social two" aria-label="Social link"></a>
    <a class="social three" aria-label="Social link"></a>
    <nav class="main-nav">
      <span class="active">WHO WE ARE</span><span>WHAT WE DO</span><span>WHAT WE'VE DONE</span><span>CONTACT US</span><span>VELCARO HOME</span>
    </nav>
    <ul class="dropdown">
      <li>About us</li><li class="current">Team</li><li>News</li><li>Corporate Culture</li><li>Join our Team</li><li>Resources</li>
    </ul>
  </header>

  <section class="hero">
    <div class="hero-media" role="img" aria-label="Photo of a downtown waterfront skyline with glass office towers under a blue sky"></div>
    <div class="hero-caption">Contact us today, let us put our expertise to work for you
      <svg class="hero-arrows" viewBox="0 0 28 18"><path d="M9 2 3 9l6 7M19 2l6 7-6 7" stroke="#fff" stroke-width="2.6" fill="none"/></svg>
    </div>
    <form class="consult">
      <h2>CALL FOR A FREE CONSULTATION</h2>
      <div class="field"><div class="ico"><svg viewBox="0 0 16 16"><circle cx="8" cy="5" r="3" fill="#fff"/><path d="M2 14c0-4 12-4 12 0z" fill="#fff"/></svg></div><span>Name</span></div>
      <div class="field"><div class="ico"><svg viewBox="0 0 16 16"><rect x="1.5" y="3.5" width="13" height="9" fill="none" stroke="#fff" stroke-width="1.4"/><path d="M1.5 3.5 8 9l6.5-5.5" fill="none" stroke="#fff" stroke-width="1.4"/></svg></div><span>Email</span></div>
      <div class="field"><div class="ico"><svg viewBox="0 0 16 16"><rect x="1" y="1" width="14" height="14" rx="2" fill="#fff"/><path d="M5 3.5c.8 0 1.5 1.8 1.2 2.3l-.6.8c.6 1.3 1.6 2.4 2.9 3l.7-.7c.5-.4 2.3.4 2.3 1.2 0 1-1.1 2.1-2.2 1.7C6.6 11 4.7 9.1 3.9 6.2 3.5 5 4 3.5 5 3.5z" fill="#f9a63a"/></svg></div><span>Phone</span></div>
      <div class="field tall"><div class="ico big"><svg viewBox="0 0 20 20"><text x="10" y="18" text-anchor="middle" font-family="Roboto,sans-serif" font-size="22" font-weight="500" fill="#fff">?</text></svg></div><span>Your question?</span></div>
      <div class="submit">Submit</div>
    </form>
    <div class="newsletter">
      <h3>NEWLETTER SUBSCRIBER</h3>
      <div class="news-row"><div class="news-input">Enter Your Mail Id</div><div class="news-btn">Subscriber</div></div>
    </div>
  </section>
  <div class="hero-shadow"></div>

  <section class="services">
    <article class="service" style="left:101px;top:0">
      <div class="photo" role="img" aria-label="Photo of a grey two-storey family house with a garage" style="background:linear-gradient(180deg,#7fa7dc 0%,#a8b4c2 35%,#7e7c7e 70%,#c9c7c2 100%)"></div>
      <h3>FOR OWNERS</h3>
      <p>Lorem Ipsum is simply dummy text of the printing and typesetting industry. Lorem Ipsum has been the indus-try's standard dummy text ever since the 1500s, when an unknown printer took a galley of type and vived not only five centuries,</p>
    </article>
    <article class="service" style="left:439px;top:0">
      <div class="photo" role="img" aria-label="Photo of a business meeting with a small model house on a glass table" style="width:318px;background:linear-gradient(135deg,#2d3440 0%,#8c939b 40%,#dfe6ea 70%,#b9c9cf 100%)"></div>
      <h3>FOR BUYER/ DEVELOPERS</h3>
      <p style="padding-left:2px">Lorem Ipsum is simply dummy text of the printing and typesetting industry. Lorem Ipsum has been the indus-try's standard dummy text ever since the 1500s, when an unknown printer took a galley of type and vived not only five centuries,</p>
    </article>
    <article class="service" style="left:781px;top:0">
      <div class="photo" role="img" aria-label="Photo of open hands holding a glowing house outline on a dark background" style="background:linear-gradient(135deg,#141a28 0%,#2d3a55 50%,#141a28 100%)"></div>
      <h3>FOR LENDERS</h3>
      <p style="padding-left:2px">Lorem Ipsum is simply dummy text of the printing and typesetting industry. Lorem Ipsum has been the indus-try's standard dummy text ever since the 1500s, when an unknown printer took a galley of type and vived not only five centuries,</p>
    </article>
  </section>

  <footer class="site-footer">
    <div class="footer-brand"><span class="brand-mark"></span><span class="brand-name">VELCARO</span></div>
    <div class="copyright">Copyright © 2014 All Rights</div>
    <div class="address">Velcaro • 4210 Harbor Crest Avenue Suite 210 • San Diego, California 92101<br>Tel: 1.619.555.0148 • Fax: 1.619.555.0190</div>
  </footer>
</div>
</body>
</html>
```